Harrow Glen Kentucky Bourbon Whiskey

We need a label design for a bottle of whiskey. It is for a 750 ml bottle and needs to have a place to write in proof, age, and bottle number at bottom of label. It is a single barrel bourbon. We want to include our tree logo attached in the upload files in some way. Leave out the Distillery part to where it just says Harrow Glen Bourbon Whiskey with the tree. We need the label to be clean and modern. I have also attached a picture of the bottle the label is intended to go on.

Industry/Entity Type

Bourbon

Requirements
Must have
• Harrow Glen tree from file

```html
<!DOCTYPE html>
<html lang="en">
<head>
<meta charset="utf-8">
<title>Harrow Glen Single Barrel Bourbon Whiskey – Label</title>
<link rel="stylesheet" href="https://fonts.googleapis.com/css2?family=Josefin+Sans:wght@400;600&family=Montserrat:wght@500;600&family=Allura&display=swap">
<style>
  :root {
    --backdrop: #e9e6e1;
    --label-cream: #f4eee1;
    --label-edge: #fbf9f4;
    --whiskey-red: #7b1c15;
    --whiskey-red-deep: #5e120d;
    --band-text: #fbf3ea;
    --mark-grey: #d9d4ca;
    --rule-grey: #b9b2a8;
  }
  * { margin: 0; padding: 0; box-sizing: border-box; }
  html, body {
    width: 1200px; height: 1000px; overflow: hidden;
    background: var(--backdrop);
  }
  .canvas { position: relative; width: 1200px; height: 1000px; }

  .label {
    position: absolute; left: 120px; top: 85px;
    width: 960px; height: 830px;
    background: var(--label-cream);
    border: 6px solid var(--label-edge);
    border-radius: 64px;
  }
  .label-frame {
    position: absolute; inset: 22px;
    border: 7px solid var(--whiskey-red);
    border-radius: 48px;
  }

  .brand-mark {
    position: absolute; left: 0; right: 0; top: 360px; height: 300px;
    display: flex; align-items: center; justify-content: center;
    font-family: "Montserrat", sans-serif; font-weight: 600;
    font-size: 84px; letter-spacing: 6px;
    color: var(--mark-grey);
  }

  .eyebrow {
    position: absolute; left: 0; right: 0; top: 150px;
    text-align: center;
    font-family: "Montserrat", sans-serif; font-weight: 600;
    font-size: 22px; letter-spacing: 9px;
    color: var(--whiskey-red);
  }
  .title-band {
    position: absolute; left: 120px; top: 182px;
    width: 720px; height: 132px;
    border-radius: 24px;
    background: linear-gradient(180deg, var(--whiskey-red) 0%, var(--whiskey-red-deep) 100%);
    display: flex; align-items: center; justify-content: center;
  }
  .title-band h1 {
    font-family: "Josefin Sans", sans-serif; font-weight: 400;
    font-size: 104px; letter-spacing: 14px; line-height: 1;
    padding-top: 14px; padding-left: 14px;
    color: var(--band-text);
  }
  .subtitle {
    position: absolute; left: 0; right: 0; top: 330px;
    text-align: center;
    font-family: "Montserrat", sans-serif; font-weight: 500;
    font-size: 36px; letter-spacing: 12px;
    color: var(--whiskey-red);
  }

  .fill-fields {
    position: absolute; left: 270px; top: 500px; width: 400px;
    list-style: none;
  }
  .fill-fields li {
    position: relative; height: 65px;
    display: flex; align-items: flex-end;
    border-bottom: 2px solid var(--rule-grey);
    font-family: "Allura", cursive;
    font-size: 40px; line-height: 1;
    color: var(--whiskey-red);
  }
  .drop-icon {
    position: absolute; left: 650px; top: 552px;
    width: 22px; height: 30px;
  }

  .volume {
    position: absolute; left: 0; right: 0; top: 748px;
    text-align: center;
    font-family: "Josefin Sans", sans-serif; font-weight: 600;
    font-size: 36px; letter-spacing: 1px;
    color: var(--whiskey-red);
  }
</style>
</head>
<body>
<main class="canvas">
  <section class="label" aria-label="Harrow Glen Single Barrel Bourbon Whiskey bottle label">
    <div class="label-frame"></div>

    <div class="brand-mark">Harrow Glen</div>

    <p class="eyebrow">SINGLE BARREL</p>
    <div class="title-band"><h1>BOURBON</h1></div>
    <p class="subtitle">WHISKEY</p>

    <ul class="fill-fields">
      <li>Proof</li>
      <li>Age</li>
      <li>Bottle No</li>
    </ul>

    <svg class="drop-icon" viewBox="0 0 22 30" aria-hidden="true">
      <path d="M11 1 C11 1 2 14 2 20 a9 9 0 0 0 18 0 C20 14 11 1 11 1 Z" fill="#7b1c15"/>
    </svg>

    <p class="volume">750ML</p>
  </section>
</main>
</body>
</html>
```